Business Card - Existing Logo & Branding copied to Business Card Format

We are looking for a designer to help with designing a two sided business card for us. We sell a web based software platform that helps people sell access to online training.
We have an existing logo and recently completed a design project here on draft hive to have someone design a nice trade show booth for us (also attached file for that design as well as our logo). We really like the look and feel of the tradeshow booth design. The fonts, colors, etc all work for us. We are hoping someone can create something very similar just in business card format.
Should be pretty straight forward hopefully....
On one side we want the logo, employee name, email address, phone and fax. On the other side we would like the text "transform your organizations training, revenue products = revenue" - See the attached PSD for what we want that to look like.
You can also see our website at www.tutorvane.com for an example of our branding.
We are open to ideas, have done several projects on draft hive and love when designers come up with creative approaches that are even better then what we envisioned.
Software

```html
<!DOCTYPE html>
<html lang="en">
<head>
<meta charset="utf-8">
<title>TutorVane Business Card</title>
<link rel="stylesheet" href="https://fonts.googleapis.com/css2?family=Poppins:wght@500;600&family=Open+Sans:wght@400;600&family=Special+Elite&display=swap">
<style>
  :root {
    --brand-red: #c1202f;
    --ink: #3a3a3a;
    --paper: #ffffff;
    --backdrop: #d9d9d9;
  }
  * { margin: 0; padding: 0; box-sizing: border-box; }
  html, body { width: 1200px; height: 900px; overflow: hidden; }
  body {
    background: var(--backdrop);
    font-family: "Open Sans", Arial, sans-serif;
    position: relative;
  }
  .card {
    position: absolute;
    top: 295px;
    width: 540px;
    height: 310px;
    background: var(--paper);
    overflow: hidden;
    box-shadow: 0 4px 14px rgba(0,0,0,0.18);
  }
  .card--back { left: 40px; }
  .card--front { left: 620px; }
  .card__band { position: absolute; inset: 0; width: 100%; height: 100%; }

  /* Back side */
  .back__name {
    position: absolute; left: 30px; top: 28px;
    font-family: "Poppins", sans-serif; font-weight: 600;
    font-size: 68px; letter-spacing: -2px; line-height: 1;
    color: var(--ink);
  }
  .back__tagline {
    position: absolute; left: 30px; top: 104px;
    font-family: "Open Sans", sans-serif; font-weight: 600;
    font-size: 16px; color: var(--ink);
  }
  .back__claim {
    position: absolute; left: 30px; top: 128px;
    font-family: "Special Elite", monospace;
    font-size: 16px; line-height: 1.3; color: var(--brand-red);
    letter-spacing: 1px;
  }
  .back__claim .plain { color: var(--ink); }
  .back__equals {
    position: absolute; left: 345px; top: 130px;
    font-family: "Special Elite", monospace; font-size: 26px; color: var(--ink);
  }
  .back__result {
    position: absolute; left: 380px; top: 134px;
    font-family: "Special Elite", monospace; font-size: 22px; color: var(--ink);
  }
  .back__web {
    position: absolute; left: 36px; top: 183px;
    font-family: "Poppins", sans-serif; font-weight: 500;
    font-size: 22px; color: var(--ink);
  }

  /* Front side */
  .front__brand {
    position: absolute; left: 36px; top: 22px;
    display: flex; align-items: center; gap: 18px;
  }
  .front__mark { width: 62px; height: 62px; background: var(--brand-red); }
  .front__name {
    font-family: "Poppins", sans-serif; font-weight: 600;
    font-size: 46px; letter-spacing: -1px; color: var(--ink);
  }
  .front__person {
    position: absolute; left: 90px; top: 100px; color: #111;
  }
  .front__person-name { font-size: 28px; line-height: 1.2; }
  .front__person-role { font-size: 20px; }
  .front__contacts, .front__address {
    position: absolute; top: 220px; list-style: none;
    color: var(--paper); font-size: 14.5px; line-height: 1.45;
  }
  .front__contacts { left: 48px; }
  .front__address { left: 340px; }
  .front__contacts li, .front__address li { display: flex; align-items: center; gap: 8px; }
  .icon { width: 13px; height: 13px; flex: none; fill: var(--paper); }
  .front__address .indent { padding-left: 21px; }
</style>
</head>
<body>

  <section class="card card--back" aria-label="Business card back">
    <svg class="card__band" viewBox="0 0 540 310" aria-hidden="true">
      <path d="M0,252 Q290,238 540,140 L540,310 L0,310 Z" fill="var(--brand-red)"/>
      <rect x="180" y="230" width="17" height="80" fill="var(--paper)"/>
      <rect x="362" y="222" width="17" height="88" fill="var(--paper)"/>
    </svg>
    <div class="back__name">TutorVane</div>
    <p class="back__tagline">Transform your organization's</p>
    <p class="back__claim">TRAINING INFORMATION<br><span class="plain">and</span> PRODUCTS</p>
    <span class="back__equals">=</span>
    <span class="back__result">Revenue</span>
    <p class="back__web">www.tutorvane.com</p>
  </section>

  <section class="card card--front" aria-label="Business card front">
    <svg class="card__band" viewBox="0 0 540 310" aria-hidden="true">
      <path d="M0,215 Q270,205 540,100 L540,310 L0,310 Z" fill="var(--brand-red)"/>
    </svg>
    <div class="front__brand">
      <span class="front__mark"></span>
      <span class="front__name">TutorVane</span>
    </div>
    <div class="front__person">
      <p class="front__person-name">Alan Reed</p>
      <p class="front__person-role">Director</p>
    </div>
    <ul class="front__contacts">
      <li><svg class="icon" viewBox="0 0 12 12"><path d="M3 0h6a1 1 0 0 1 1 1v10a1 1 0 0 1-1 1H3a1 1 0 0 1-1-1V1a1 1 0 0 1 1-1zm0 2v7h6V2z"/></svg>800-555-0142</li>
      <li><svg class="icon" viewBox="0 0 12 12"><path d="M3 0h6v3H3zM0 4h12v5h-2v3H2V9H0zm3 4v3h6V8z"/></svg>012-555-0199</li>
      <li><svg class="icon" viewBox="0 0 12 12"><path d="M0 2h12v8H0zm1 1v.4l5 3.2 5-3.2V3z"/></svg>alanreed@tutorvane.com</li>
    </ul>
    <ul class="front__address">
      <li><svg class="icon" viewBox="0 0 12 12"><path d="M6 0a4 4 0 0 1 4 4c0 3-4 8-4 8S2 7 2 4a4 4 0 0 1 4-4zm0 2.5a1.5 1.5 0 1 0 0 3 1.5 1.5 0 0 0 0-3z"/></svg>1180 NW Harbor Ave</li>
      <li class="indent"># 318, Seattle,</li>
      <li class="indent">WA 98107</li>
    </ul>
  </section>

</body>
</html>
```